Website design for lighting products company

We want a design for our website. The website is for a company that sells lighting products. The structure is similar to the below website. We really like their design as well: www.brambleshorelamps.com

Industry/Entity Type

Lighting

Number of Pages Required

5+ page

Colors

Designer to choose colors to be used in the design.

Requirements
Must have
• Simple design

```html
<!DOCTYPE html>
<html lang="en">
<head>
<meta charset="utf-8">
<title>Brambleshore Lamps</title>
<link href="https://fonts.googleapis.com/css2?family=Montserrat:wght@300;400;500;600&display=swap" rel="stylesheet">
<style>
:root{
  --blue:#0aa3f2;
  --text:#555555;
  --muted:#8d8d8d;
  --line:#e6e6e6;
  --panel:#f9f9f9;
  --white:#ffffff;
  --hero-dark:#4a4b4d;
}
*{margin:0;padding:0;box-sizing:border-box}
html,body{width:810px;height:1200px;overflow:hidden;background:var(--white)}
body{position:relative;font-family:"Montserrat",Arial,sans-serif;color:var(--text)}
.abs{position:absolute}

.site-header{left:0;top:0;width:810px;height:57px}
.phone{right:112px;top:16px;font-size:8px;font-weight:500;color:var(--text);display:flex;align-items:center;gap:4px}
.main-nav{right:112px;top:38px;display:flex;gap:16px;font-size:7.6px;color:var(--text);letter-spacing:.1px}

.hero{left:0;top:57px;width:810px;height:268px;background:linear-gradient(180deg,#6e6e70 0%,#4d4e50 45%,#5b5b5c 100%)}
.hero-title{left:0;top:100px;width:810px;text-align:center;color:var(--white);font-size:22px;font-weight:600;line-height:27px}
.btn-outline{left:355px;top:222px;width:100px;height:25px;border:1.5px solid var(--white);border-radius:13px;color:var(--white);font-size:9px;font-weight:600;display:flex;align-items:center;justify-content:center}

.section-title{left:0;width:810px;text-align:center;font-weight:300;font-size:23px;color:var(--text)}
.title-rule{left:374px;width:63px;height:2px;background:var(--blue)}
.intro{left:212px;top:384px;width:386px;text-align:center;font-size:8.2px;line-height:12.2px;color:var(--text)}
.btn-blue{background:var(--blue);color:var(--white);border-radius:12px;font-size:9.5px;font-weight:400;display:flex;align-items:center;justify-content:center}

.products{left:0;top:506px;width:810px;height:430px;background:var(--panel)}
.product-card{width:140px;height:144px;background:var(--white);border:1px solid var(--line)}
.product-photo{position:absolute;left:28px;top:15px;width:84px;height:86px;border-radius:3px;background:radial-gradient(circle at 50% 45%,#f4f4f4 0%,#dcdcdc 60%,#f4f4f4 100%)}
.product-name{position:absolute;left:0;bottom:14px;width:100%;text-align:center;font-size:8.2px;color:var(--text)}

.subscribe-title{left:0;top:956px;width:810px;text-align:center;font-size:18px;font-weight:300;color:var(--text)}
.email-field{left:259px;top:993px;width:211px;height:25px;border:1px solid var(--line);font-size:8px;color:#aaaaaa;padding-left:9px;display:flex;align-items:center}
.subscribe-btn{left:470px;top:993px;width:84px;height:25px;background:#c4c4c4;color:var(--white);font-size:10px;display:flex;align-items:center;justify-content:center}

.footer-rule{left:0;width:810px;height:1px;background:var(--line)}
.footer-head{top:1058px;font-size:8.2px;color:var(--blue)}
.footer-list{font-size:8.2px;color:var(--muted);list-style:none}
.social{left:572px;top:1082px;display:flex;gap:9px}
.social span{width:16px;height:16px;border:1px solid #cfcfcf;border-radius:50%}
.copyright{left:0;top:1169px;width:810px;text-align:center;font-size:7.4px;color:var(--muted)}
</style>
</head>
<body>

<header class="abs site-header">
  <div class="abs phone">
    <svg width="10" height="10" viewBox="0 0 20 20" aria-hidden="true"><circle cx="10" cy="10" r="9" fill="none" stroke="#777" stroke-width="1.4"/><path d="M7 5.5l1.6 2.3-1 1.2c.6 1.3 1.6 2.3 2.9 2.9l1.2-1 2.3 1.6-.9 1.7c-3.6-.3-6.9-3.6-7.2-7.2z" fill="#777"/></svg>
    +44 5810 227416
  </div>
  <nav class="abs main-nav">
    <span>HOME</span><span>ABOUT</span><span>PRODUCTS</span><span>SOLUTIONS</span><span>NEWS</span><span>CONTACT</span>
  </nav>
</header>

<section class="abs hero" role="img" aria-label="Photo of a modern open-plan office lit by long black suspended linear lights"></section>
<h1 class="abs hero-title" style="font-size:22px">A Light For<br>Your Every Style</h1>
<div class="abs btn-outline">View Products</div>

<h2 class="abs section-title" style="top:336px">Welcome to Company</h2>
<div class="abs title-rule" style="top:369px"></div>
<p class="abs intro">Lorem Ipsum is simply dummy text of the printing and typesetting industry. Lorem Ipsum has been the industry's standard dummy text ever since the 1500s, when an unknown printer took a galley of type and scrambled it to make a type specimen book. It has survived not only five centuries, but also the leap into electronic typesetting, remaining essentially unchanged.</p>
<div class="abs btn-blue" style="left:368px;top:449px;width:73px;height:23px">About Us</div>

<section class="abs products"></section>
<h2 class="abs section-title" style="top:525px">Our Products</h2>
<div class="abs title-rule" style="top:558px"></div>

<div class="abs product-card" style="left:111px;top:579px"><div class="product-photo" role="img" aria-label="Angled white ceiling light fitting"></div><div class="product-name">Lorem ipsum doller</div></div>
<div class="abs product-card" style="left:261px;top:579px"><div class="product-photo" role="img" aria-label="Narrow recessed downlight with louvres"></div><div class="product-name">Lorem ipsum doller</div></div>
<div class="abs product-card" style="left:410px;top:579px"><div class="product-photo" role="img" aria-label="Suspended linear light bar"></div><div class="product-name">Lorem ipsum doller</div></div>
<div class="abs product-card" style="left:559px;top:579px"><div class="product-photo" role="img" aria-label="Recessed rectangular panel light"></div><div class="product-name">Lorem ipsum doller</div></div>
<div class="abs product-card" style="left:111px;top:732px"><div class="product-photo" role="img" aria-label="Angled white ceiling light fitting"></div><div class="product-name">Lorem ipsum doller</div></div>
<div class="abs product-card" style="left:261px;top:732px"><div class="product-photo" role="img" aria-label="Narrow recessed downlight with louvres"></div><div class="product-name">Lorem ipsum doller</div></div>
<div class="abs product-card" style="left:410px;top:732px"><div class="product-photo" role="img" aria-label="Suspended linear light bar"></div><div class="product-name">Lorem ipsum doller</div></div>
<div class="abs product-card" style="left:559px;top:732px"><div class="product-photo" role="img" aria-label="Recessed rectangular panel light"></div><div class="product-name">Lorem ipsum doller</div></div>

<div class="abs btn-blue" style="left:350px;top:893px;width:110px;height:23px">View All Products</div>

<h2 class="abs subscribe-title">Subscribe to news and updates</h2>
<div class="abs email-field">Enter your email address</div>
<div class="abs subscribe-btn">Subscribe</div>

<div class="abs footer-rule" style="top:1043px"></div>
<footer>
  <h3 class="abs footer-head" style="left:112px;font-weight:400">CONTACT</h3>
  <ul class="abs footer-list" style="left:111px;top:1078px;line-height:18.5px">
    <li>Telephone: 44 (0)333 618 2094</li>
    <li>Facsimile: +44 (0)333 618 2095</li>
    <li>Email: hello@brambleshorelamps.com</li>
  </ul>
  <h3 class="abs footer-head" style="left:294px;font-weight:400">USEFUL LINKS</h3>
  <ul class="abs footer-list" style="left:294px;top:1078px;line-height:13.4px">
    <li>About us</li><li>Products</li><li>Solutions</li><li>News</li>
  </ul>
  <ul class="abs footer-list" style="left:369px;top:1078px;line-height:13.4px">
    <li>Career</li><li>Contact</li><li>Terms of use</li><li>Privacy policy</li>
  </ul>
  <ul class="abs footer-list" style="left:451px;top:1078px;line-height:13.4px">
    <li>Terms &amp; Conditions</li><li>Warranty</li>
  </ul>
  <h3 class="abs footer-head" style="left:573px;font-weight:400">SOCIAL MEDIA</h3>
  <div class="abs social" aria-label="Social media links"><span></span><span></span><span></span><span></span></div>
</footer>
<div class="abs footer-rule" style="top:1154px"></div>
<p class="abs copyright">©2019 Brambleshore Lamps</p>

</body>
</html>
```